Web Design Job: Condo Debts Collection Business needs a Web Design

I need a site for a client, who works with condo debts collection, and ensure all revenues provided by condo fees will be always available to the building manager of condo on a specific date, regardless of defaults.
I have the visual identity (logo, slogan and colors) of the company, and some requirements on layout (kind of slider, menu options, phone number on a noble position, etc) - maybe I can do a sketch, but I like the idea of give some freedom to designer.

*** PLEASE, we have no interest in templates. We want something new***

Reason: We need something new, different and exclusive. We do not want anything that looks like a "template". Thanks.

Target Market(s)

I have two targets for this design:
- Condominium's building manager. This target is looking for a solution to overdue debts on it's condo.
- Residents on condominiums. This target wants to live in a better place, where their neighbors pay their condominium fees on time.

Industry/Entity Type

Business

Number of Pages Required

1 page

Requirements
Must have
• - Slider with title, some short text related, a nice image (I prefer happy and/or peaceful family, people doing business, happy friends, and so on).
• - I have a special attention to menu. I'm looking for one I can have a nice effect, more elegant, charming, kind of innovative.
• - Phone number on the top (or clearly visible).
• - Member log in area or icon on the top (or clearly visible).
• - News/articles area.
• - Modern fonts, with good quality, sans-serif on areas where reading is more intensive (prefer Google web-fonts).
• - Colors specified on attached files.
Nice to have
• - Clear background color, cause it's better to read larger texts (like articles). Dark backgrounds makes reading difficult.
• - A site with effects (like shadows, lines, curves, gradients, lights) is usually pretty.
• - I pay attention on beautiful footers.
Should not have
• - Images with a lot of money (I don't sell richness, I sell tranquility, peace, harmony, safety).
• - Poor menu.

```html
<!DOCTYPE html>
<html lang="en">
<head>
<meta charset="utf-8">
<title>Vetra Solução Cobrança</title>
<link href="https://fonts.googleapis.com/css2?family=Open+Sans:wght@400;600;700&family=Oswald:wght@400;500&display=swap" rel="stylesheet">
<style>
:root{
  --navy:#1b2a5a;
  --navy-dark:#13204a;
  --blue:#2b8fd6;
  --blue-text:#1f5fa8;
  --ink:#333;
  --muted:#666;
  --line:#dcdfe6;
  --band:#27324d;
  --footer:#2a2a2a;
  --footer-dark:#1c1c1c;
  --white:#fff;
}
*{margin:0;padding:0;box-sizing:border-box}
html,body{width:1200px;height:2568px;overflow:hidden}
body{font-family:'Open Sans',Arial,sans-serif;color:var(--ink);background:var(--white);position:relative}
.abs{position:absolute}

/* header */
.topbar{top:0;left:0;width:1200px;height:128px;background:var(--white)}
.brand{left:112px;top:22px;display:flex;align-items:center;gap:12px}
.brand-mark{width:56px;height:56px;background:var(--navy)}
.brand-name{font-weight:700;font-size:26px;color:var(--navy);letter-spacing:1px}
.contact-line{left:560px;top:68px;font-size:15px;color:var(--navy);display:flex;gap:34px;align-items:center}
.contact-line span{display:flex;align-items:center;gap:8px}
.login{left:924px;top:14px;width:180px;height:34px;background:var(--navy);color:var(--white);font-size:13px;font-weight:600;display:flex;align-items:center;justify-content:center;gap:8px;border-radius:3px}

.nav{top:128px;left:0;width:1200px;height:34px;background:var(--navy)}
.nav ul{list-style:none;display:flex;position:absolute;left:72px;top:0;height:34px}
.nav li{color:var(--white);font-size:13px;font-weight:600;padding:0 22px;line-height:34px}
.nav li.active{background:var(--blue)}
.social{display:flex;gap:8px}
.social i{display:block;width:24px;height:24px;border-radius:50%;background:var(--white)}
.nav .social{position:absolute;right:86px;top:5px}
.nav .social i{background:#7f8db5}

/* hero */
.hero{top:162px;left:0;width:1200px;height:620px;overflow:hidden}
.hero-photo{position:absolute;inset:0;background:linear-gradient(160deg,#c9b9a4 0%,#a88d76 35%,#6f6a70 70%,#3e4764 100%)}
.hero-curve{position:absolute;left:0;bottom:0}
.hero-title{position:absolute;top:420px;width:100%;text-align:center;font-family:'Oswald',sans-serif;font-size:56px;color:var(--white);letter-spacing:2px}
.hero-sub{position:absolute;top:490px;width:100%;text-align:center;font-family:'Oswald',sans-serif;font-size:34px;color:var(--white);letter-spacing:2px}
.dots{position:absolute;top:580px;left:570px;display:flex;gap:10px}
.dots i{width:12px;height:12px;border-radius:50%;background:#8895bd}
.dots i.on{background:var(--white)}

/* welcome */
.welcome{top:810px;left:72px;width:760px}
h2.section-title{font-size:24px;font-weight:700;color:var(--navy);text-transform:uppercase;letter-spacing:.5px}
.welcome h2{margin-bottom:16px}
.welcome .lead{font-size:13px;color:var(--blue-text);text-transform:uppercase;margin-bottom:10px;font-weight:600}
.welcome p{font-size:13px;line-height:21px;color:var(--muted);margin-bottom:12px}
.news{top:810px;left:900px;width:232px}
.news h2{margin-bottom:20px}
.news-item{margin-bottom:18px;font-size:12px;line-height:17px}
.news-item .date{color:var(--muted);font-size:11px}
.news-item b{color:var(--navy);display:block}
.news-item p{color:var(--muted)}

/* services */
.services{top:1348px;left:0;width:1200px;height:440px;background:linear-gradient(180deg,#3a4566,#1f2944)}
.services h2{position:absolute;top:40px;width:100%;text-align:center;font-size:24px;color:var(--white);font-weight:600;letter-spacing:1px}
.services h2:after{content:"";display:block;width:60px;height:2px;background:var(--blue);margin:10px auto 0}
.card{position:absolute;top:110px;width:316px}
.card .pic{height:126px;border:4px solid var(--white)}
.card h3{color:var(--white);font-size:15px;line-height:21px;font-weight:700;margin-top:16px}
.card .more{color:var(--white);font-size:13px;margin-top:14px;display:flex;align-items:center;gap:6px}

/* proposal */
.proposal{top:1858px;left:72px;width:328px;height:408px;background:#f2f3f6;border:1px solid var(--line)}
.proposal .head{height:52px;background:var(--navy);color:var(--white);font-weight:700;font-size:20px;line-height:52px;padding-left:22px}
.proposal form{padding:18px 22px}
.field{height:36px;border:1px solid #cfd3db;background:var(--white);margin-bottom:12px;font-size:12px;color:#999;padding:9px 10px}
.field.msg{height:92px}
.submit{width:104px;height:34px;background:var(--blue);color:var(--white);font-size:13px;font-weight:700;text-align:center;line-height:34px}
.pitch{top:1870px;left:440px;width:700px}
.pitch h2{font-size:22px;line-height:30px;color:var(--navy);font-weight:700;text-transform:uppercase}
.pitch h4{font-size:14px;color:var(--blue-text);margin:14px 0 24px;text-transform:uppercase}
.pitch h5{font-size:14px;color:var(--navy);margin-bottom:10px;text-transform:uppercase}
.pitch ul{list-style:none}
.pitch li{font-size:13px;color:var(--muted);line-height:25px;display:flex;align-items:center;gap:8px}

/* footer */
.footer{top:2306px;left:0;width:1200px;height:262px;background:var(--footer);color:#ccc}
.ask{position:absolute;left:72px;top:10px;height:72px;width:1056px;display:flex;align-items:center}
.ask .q{font-family:'Oswald',sans-serif;font-size:22px;line-height:22px;color:var(--white);width:200px}
.ask .it{display:flex;align-items:center;gap:10px;font-size:11px;line-height:14px;color:var(--white);width:214px}
.ask .ic{width:36px;height:36px;border-radius:50%;border:2px solid #777;display:flex;align-items:center;justify-content:center}
.cols{position:absolute;left:72px;top:94px;width:1056px;display:flex;gap:0;border-top:1px solid #3d3d3d;padding-top:14px}
.col{width:264px;font-size:11px;line-height:17px}
.col h6{color:var(--white);font-size:11px;margin-bottom:10px;text-transform:uppercase}
.col .in{width:140px;height:22px;background:var(--white);margin-top:8px;color:#999;padding:3px 6px}
.col .go{width:60px;height:20px;background:var(--blue);margin-top:6px;color:var(--white);text-align:center;line-height:20px}
.col .social i{background:#888}
.bottom{position:absolute;bottom:0;left:0;width:1200px;height:28px;background:var(--footer-dark);font-size:11px;color:#aaa;text-align:center;line-height:28px}
</style>
</head>
<body>

<header class="abs topbar">
  <div class="abs brand"><div class="brand-mark"></div><span class="brand-name">VSC</span></div>
  <div class="abs login">
    <svg width="12" height="12" viewBox="0 0 12 12"><circle cx="6" cy="4" r="2.6" fill="#fff"/><path d="M1 12a5 5 0 0 1 10 0z" fill="#fff"/></svg>
    MEMBER LOGIN
  </div>
  <div class="abs contact-line">
    <span><svg width="14" height="14" viewBox="0 0 14 14"><path d="M3 1l2 3-1.3 1.3a7 7 0 0 0 5 5L10 9l3 2-1.4 2A10 10 0 0 1 1 2.4z" fill="#1b2a5a"/></svg>(31) 4410-2285 | (31) 4410-7731</span>
    <span><svg width="14" height="10" viewBox="0 0 14 10"><rect x=".5" y=".5" width="13" height="9" fill="none" stroke="#1b2a5a"/><path d="M.5.5l6.5 5 6.5-5" fill="none" stroke="#1b2a5a"/></svg>contato@vetracobranca.com.br</span>
  </div>
</header>

<nav class="abs nav">
  <ul>
    <li class="active">HOME</li><li>ABOUT</li><li>YOUR CLP?</li><li>SERVICES</li><li>NEWS</li><li>PARTNERS</li><li>CONTACT</li>
  </ul>
  <div class="social"><i></i><i></i><i></i></div>
</nav>

<section class="abs hero">
  <div class="hero-photo" role="img" aria-label="Photo of a group of happy friends laughing together outdoors"></div>
  <svg class="hero-curve" width="1200" height="140" viewBox="0 0 1200 140" preserveAspectRatio="none">
    <path d="M0 40 Q600 150 1200 40 L1200 140 L0 140Z" fill="#1b2a5a" opacity=".85"/>
  </svg>
  <div class="hero-title">LOREM IPSUM DOLOR SIT AMET</div>
  <div class="hero-sub">CONSECTETUR ADIPISCING ELIT</div>
  <div class="dots"><i></i><i class="on"></i><i></i></div>
</section>

<section class="abs welcome">
  <h2 class="section-title">Welcome to Vetra Solução Cobrança</h2>
  <p class="lead">Cobrança garantida de condomínios</p>
  <p class="lead">Quer receber todas as taxas do seu condomínio em dia e ainda aumentar sua receita?</p>
  <p>A Vetra Solução Cobrança é uma empresa que faz a cobrança das inadimplências do seu condomínio. Todo mês, na data de vencimento das taxas condominiais, depositamos na conta do condomínio o valor total das cotas, independentemente de atrasos. Assim o síndico garante o caixa para pagar os serviços e fornecedores do prédio sem surpresas e com total tranquilidade para todos os moradores.</p>
  <p>A Vetra assume a gestão completa da inadimplência, desde a notificação amigável até a negociação final com o condômino devedor, preservando a boa convivência entre vizinhos.</p>
  <p>Pensou em uma solução segura e simples? Fale conosco e conheça as vantagens de ter o recebimento garantido todos os meses no seu condomínio.</p>
</section>

<aside class="abs news">
  <h2 class="section-title">Latest News / Articles</h2>
  <div class="news-item"><span class="date">10/07/2015</span><b>Lorem ipsum dolor sit amet, consectetur adipiscing elit,</b><p>sed do eiusmod tempor incididunt ut labore et dolore magna aliqua.</p></div>
  <div class="news-item"><span class="date">08/07/2015</span><b>Lorem ipsum dolor sit amet, consectetur adipiscing elit,</b><p>sed do eiusmod tempor incididunt ut labore et dolore magna aliqua.</p></div>
  <div class="news-item"><span class="date">02/07/2015</span><b>Lorem ipsum dolor sit amet, consectetur adipiscing elit,</b><p>sed do eiusmod tempor incididunt ut labore et dolore magna aliqua.</p></div>
  <div class="news-item"><span class="date">28/06/2015</span><b>Lorem ipsum dolor sit amet, consectetur adipiscing elit,</b><p>sed do eiusmod tempor incididunt ut labore et dolore magna aliqua.</p></div>
</aside>

<section class="abs services">
  <h2>OUR SERVICES</h2>
  <div class="card" style="left:72px">
    <div class="pic" role="img" aria-label="Photo of a building manager meeting with residents" style="background:linear-gradient(135deg,#8fa3bd,#4d5d7a)"></div>
    <h3>Lorem ipsum dolor sit amet, consectetur adipiscing elit</h3>
    <div class="more">Read more <svg width="10" height="10" viewBox="0 0 10 10"><path d="M2 1l5 4-5 4" fill="none" stroke="#fff" stroke-width="2"/></svg></div>
  </div>
  <div class="card" style="left:442px">
    <div class="pic" role="img" aria-label="Photo of people doing business at a desk" style="background:linear-gradient(135deg,#a7b4c6,#566683)"></div>
    <h3>Lorem ipsum dolor sit amet, consectetur adipiscing elit</h3>
    <div class="more">Read more <svg width="10" height="10" viewBox="0 0 10 10"><path d="M2 1l5 4-5 4" fill="none" stroke="#fff" stroke-width="2"/></svg></div>
  </div>
  <div class="card" style="left:812px">
    <div class="pic" role="img" aria-label="Photo of a team working together around a table" style="background:linear-gradient(135deg,#c2b59d,#6b6f7e)"></div>
    <h3>Lorem ipsum dolor sit amet, consectetur adipiscing elit</h3>
    <div class="more">Read more <svg width="10" height="10" viewBox="0 0 10 10"><path d="M2 1l5 4-5 4" fill="none" stroke="#fff" stroke-width="2"/></svg></div>
  </div>
</section>

<section class="abs proposal">
  <div class="head">ASK FOR YOUR PROPOSAL</div>
  <form>
    <div class="field">Name</div>
    <div class="field">E-mail</div>
    <div class="field">Phone</div>
    <div class="field msg">Message</div>
    <div class="submit">SUBMIT</div>
  </form>
</section>

<section class="abs pitch">
  <h2>Conheça a Vetra Solução Cobrança e solucione seus problemas</h2>
  <h4>Conheça a Vetra Solução Cobrança e solucione seus problemas</h4>
  <h5>Vantagens de ser um cliente Vetra:</h5>
  <ul>
    <li><svg width="12" height="12" viewBox="0 0 12 12"><path d="M1 6l3 3 7-7" fill="none" stroke="#2b8fd6" stroke-width="2"/></svg>Antecipação de 100% do valor da cobrança na data do vencimento</li>
    <li><svg width="12" height="12" viewBox="0 0 12 12"><path d="M1 6l3 3 7-7" fill="none" stroke="#2b8fd6" stroke-width="2"/></svg>Desoneração do síndico na cobrança dos inadimplentes</li>
    <li><svg width="12" height="12" viewBox="0 0 12 12"><path d="M1 6l3 3 7-7" fill="none" stroke="#2b8fd6" stroke-width="2"/></svg>Equilíbrio permanente do caixa para pagar fornecedores em dia</li>
    <li><svg width="12" height="12" viewBox="0 0 12 12"><path d="M1 6l3 3 7-7" fill="none" stroke="#2b8fd6" stroke-width="2"/></svg>Antecipação de receita para obras e melhorias no condomínio</li>
    <li><svg width="12" height="12" viewBox="0 0 12 12"><path d="M1 6l3 3 7-7" fill="none" stroke="#2b8fd6" stroke-width="2"/></svg>Atendimento dedicado e relatórios mensais transparentes</li>
    <li><svg width="12" height="12" viewBox="0 0 12 12"><path d="M1 6l3 3 7-7" fill="none" stroke="#2b8fd6" stroke-width="2"/></svg>Diminuição dos conflitos entre vizinhos e mais harmonia</li>
  </ul>
</section>

<footer class="abs footer">
  <div class="ask">
    <div class="q">HAVE<br>QUESTIONS?</div>
    <div class="it"><div class="ic"><svg width="14" height="14" viewBox="0 0 14 14"><path d="M3 1l2 3-1.3 1.3a7 7 0 0 0 5 5L10 9l3 2-1.4 2A10 10 0 0 1 1 2.4z" fill="#fff"/></svg></div>CALL US<br>(31) 4410-2285</div>
    <div class="it"><div class="ic"><svg width="14" height="10" viewBox="0 0 14 10"><rect x=".5" y=".5" width="13" height="9" fill="none" stroke="#fff"/><path d="M.5.5l6.5 5 6.5-5" fill="none" stroke="#fff"/></svg></div>SEND US<br>AN EMAIL</div>
    <div class="it"><div class="ic"><svg width="12" height="16" viewBox="0 0 12 16"><path d="M6 15S1 9 1 6a5 5 0 0 1 10 0c0 3-5 9-5 9z" fill="#fff"/><circle cx="6" cy="6" r="2" fill="#2a2a2a"/></svg></div>FIND A<br>LOCAL OFFICE</div>
    <div class="it"><div class="ic"><svg width="10" height="14" viewBox="0 0 10 14"><path d="M1 1h8v12H1z" fill="none" stroke="#fff"/></svg></div>READ THE<br>FAQS</div>
  </div>
  <div class="cols">
    <div class="col"><h6>Contact us</h6>Rua das Acácias, 120<br>Centro<br>Cidade Nova/MG</div>
    <div class="col"><h6>Subscribe our newsletter</h6>Receive our latest news.<div class="in">Enter your email</div><div class="go">SEND</div></div>
    <div class="col"><h6>Quick links</h6>Home<br>About<br>Your Clp<br>Services<br>News<br>Partners<br>Contact</div>
    <div class="col"><h6>Connect with us</h6><div class="social"><i></i><i></i><i></i></div></div>
  </div>
  <div class="bottom">© 2015 Vetra. All Rights Reserved &nbsp;•&nbsp; Terms and Conditions &nbsp;•&nbsp; Privacy Policy &nbsp;•&nbsp; Terms of Use</div>
</footer>

</body>
</html>
```